CD Cover Design for BRISK TOFFEE

We need a groovy cover design for a new comedy CD called "Brisk Toffee." We have in mind a retro 1960s-70s feel based on the subject material of the CD, but we are open to other ideas.

In the title track, the comedian discusses candy from the past like Rosa Belles, Comet Blazers, Plum Tops, Zippy Tubes, Wax Candies, Candy Cigarettes, Candy Necklaces, etc. These specific candies do not need to be depicted, but we include them here as explanation for the name.

Target Market(s)

Men & Women, ages 25-85, but primarily over 40

Industry/Entity Type

Comedian

Requirements
Must have
• Front & Back Cover designs, both square format
• Front Cover - Title: "Brisk Toffee"
• Back Cover - Photo of Comedian (use one of the photos uploaded)
• Back Cover - Tracks listed as follows:
• 1 – Field Hockey / Parenting
• 2 – Teenagers
• 3 – Parent Teacher Conferences
• 4 – Maine
• 5 – Criminals
• 6 – Over 50
• 7 – Fun Procedure
• 8 – Guardian Donkey
• 9 – Hearthside Weekly
• 10 – 20th Anniversary
• 11 – Not a Nagger
• 12 – Travel
• 13 – Old School / Playground
• 14 – Brisk Toffee
• 15 – Cease & Desist
• 16 – Bra Shopping
• 17 – Craft Mania
• 18 – MRI Questions
• 19 – Vasectomy
Nice to have
• Retro/Vintage feel, 1960s-70s
• Original illustrations of "Brisk Toffee" would be greatly appreciated
Should not have
• Candy hearts with words

```html
<!DOCTYPE html>
<html lang="en">
<head>
<meta charset="utf-8">
<title>Brisk Toffee – CD Cover</title>
<link rel="stylesheet" href="https://fonts.googleapis.com/css2?family=Comfortaa:wght@500;600&display=swap">
<style>
  :root {
    --stage: #000000;
    --fabric-dark: #3a2a12;
    --fabric-mid: #7a4a1c;
    --fabric-warm: #b8621f;
    --fabric-olive: #8a7a2a;
    --fabric-cream: #d9c7a0;
    --polaroid: #efe8d8;
    --polaroid-shadow: rgba(0,0,0,0.45);
    --title-ink: #6b5624;
    --track-ink: #f5c21a;
    --photo-front-a: #d98a3a;
    --photo-front-b: #6a3a18;
    --photo-back-a: #e9b27a;
    --photo-back-b: #7a3218;
  }
  html, body {
    margin: 0;
    padding: 0;
    width: 1200px;
    height: 1000px;
    overflow: hidden;
    background: var(--stage);
  }
  .canvas {
    position: relative;
    width: 1200px;
    height: 1000px;
    background: var(--stage);
    font-family: "Comfortaa", sans-serif;
  }
  .cover {
    position: absolute;
    top: 218px;
    width: 563px;
    height: 563px;
    overflow: hidden;
  }
  .cover--front { left: 36px; }
  .cover--back  { left: 611px; }
  .fabric {
    position: absolute;
    inset: 0;
    background:
      radial-gradient(circle at 20% 25%, var(--fabric-warm) 0, transparent 18%),
      radial-gradient(circle at 75% 70%, var(--fabric-warm) 0, transparent 16%),
      radial-gradient(circle at 70% 15%, var(--fabric-olive) 0, transparent 14%),
      radial-gradient(circle at 25% 80%, var(--fabric-olive) 0, transparent 15%),
      linear-gradient(135deg, var(--fabric-mid), var(--fabric-dark) 50%, var(--fabric-mid));
  }
  .polaroid {
    position: absolute;
    background: var(--polaroid);
    box-shadow: 3px 5px 10px var(--polaroid-shadow);
  }
  .polaroid--front {
    left: 90px;
    top: 88px;
    width: 395px;
    height: 390px;
    transform: rotate(-16deg);
  }
  .polaroid--front .polaroid__photo {
    position: absolute;
    left: 22px;
    top: 22px;
    width: 351px;
    height: 296px;
    background: linear-gradient(160deg, var(--photo-front-a), var(--photo-front-b));
  }
  .album-title {
    position: absolute;
    left: 0;
    right: 0;
    bottom: 14px;
    margin: 0;
    text-align: center;
    font-size: 40px;
    font-weight: 600;
    letter-spacing: 3px;
    color: var(--title-ink);
  }
  .polaroid--back {
    left: 255px;
    top: 148px;
    width: 250px;
    height: 290px;
    transform: rotate(-17deg);
  }
  .polaroid--back .polaroid__photo {
    position: absolute;
    left: 16px;
    top: 16px;
    width: 218px;
    height: 218px;
    background: linear-gradient(150deg, var(--photo-back-a), var(--photo-back-b));
  }
  .tracklist {
    position: absolute;
    left: 10px;
    top: 18px;
    margin: 0;
    padding: 0;
    list-style: none;
    z-index: 2;
  }
  .tracklist li {
    font-size: 21px;
    font-weight: 600;
    line-height: 27.4px;
    letter-spacing: 2.5px;
    color: var(--track-ink);
    white-space: nowrap;
    text-transform: uppercase;
  }
</style>
</head>
<body>
<main class="canvas">
  <section class="cover cover--front">
    <div class="fabric" role="img" aria-label="Retro 1970s orange, brown and olive floral fabric pattern"></div>
    <figure class="polaroid polaroid--front">
      <div class="polaroid__photo" role="img" aria-label="Warm-toned photo of beetles beside a toilet paper roll on a desk"></div>
      <h1 class="album-title">BRISK TOFFEE</h1>
    </figure>
  </section>

  <section class="cover cover--back">
    <div class="fabric" role="img" aria-label="Retro 1970s orange, brown and olive floral fabric pattern"></div>
    <figure class="polaroid polaroid--back">
      <div class="polaroid__photo" role="img" aria-label="Vintage sepia childhood photo of the comedian with a sibling"></div>
    </figure>
    <ol class="tracklist">
      <li>1. Field Hockey/Parenting</li>
      <li>2. Teenagers</li>
      <li>3. Parent Teacher Conferences</li>
      <li>4. Maine</li>
      <li>5. Criminals</li>
      <li>6. Over 50</li>
      <li>7. Fun Procedure</li>
      <li>8. Guardian Donkey</li>
      <li>9. Hearthside Weekly</li>
      <li>10. 20th Anniversary</li>
      <li>11. Not a Nagger</li>
      <li>12. Travel</li>
      <li>13. Old School Playground</li>
      <li>14. Brisk Toffee</li>
      <li>15. Cease and Desist</li>
      <li>16. Bra Shopping</li>
      <li>17. Craft Mania</li>
      <li>18. MRI Questions</li>
      <li>19. Vasectomy</li>
    </ol>
  </section>
</main>
</body>
</html>
```